Startup company business card (Media & Advertising)

we need a business card design for a company that is a startup in the media and aggregation industry. Card needs to look funky and of a new breed/modern and upmarket.

Target Market(s)

advertisers/ brand agencies & media publishers

Industry/Entity Type

Advertising

Contact Information for Business Card

Please ensure the front face signifies our brand (plintovo.com) and back has details for the contact. Standard contact such as phone , address, email , website etc.

Font styles to use
Other font styles liked:
• use styleguide and logo font and color

Colors

Designer to choose colors to be used in the design.

Requirements
Must have
• We are disrupting the media and agency industry so subtlety would be good to use imagery to signify this
Nice to have
• Please use logo colors for branding
Should not have
• be as creative and provide few options. Pick a brand color from logo and styleguide

```html
<!DOCTYPE html>
<html lang="en">
<head>
<meta charset="utf-8">
<title>plintovo business card</title>
<link href="https://fonts.googleapis.com/css2?family=Roboto:wght@400;500;700&display=swap" rel="stylesheet">
<style>
  :root {
    --stage: #2b2b2b;
    --card-dark: #050505;
    --card-light: #ffffff;
    --brand-red: #d7263d;
    --name-red: #b81d3a;
    --ink: #1a1a1a;
    --ink-soft: #333333;
    --rule: #555555;
    --on-dark: #ffffff;
  }
  * { box-sizing: border-box; margin: 0; padding: 0; }
  html, body { width: 1200px; height: 880px; overflow: hidden; }
  body {
    background: var(--stage);
    font-family: "Roboto", Arial, sans-serif;
    position: relative;
  }
  .card {
    position: absolute;
    width: 600px;
    height: 343px;
    border-radius: 18px;
    box-shadow: 0 18px 40px rgba(0,0,0,0.45);
  }
  .card--front {
    left: 90px; top: 70px;
    background: var(--card-dark);
    display: flex; align-items: center; justify-content: center;
  }
  .card--back {
    left: 510px; top: 467px;
    background: var(--card-light);
    display: flex; align-items: center;
  }
  .brand {
    display: flex; align-items: center; gap: 18px;
  }
  .brand__dot {
    width: 46px; height: 46px; border-radius: 50%;
    background: var(--brand-red);
  }
  .brand__name {
    font-weight: 700;
    font-size: 66px;
    letter-spacing: -1px;
    color: var(--on-dark);
  }
  .card--back .brand { margin-left: 60px; width: 250px; gap: 12px; }
  .card--back .brand__dot { width: 30px; height: 30px; }
  .card--back .brand__name { font-size: 42px; color: var(--ink); }
  .divider {
    width: 1px; height: 150px;
    background: var(--rule);
    margin: 0 28px 0 12px;
  }
  .contact { color: var(--ink-soft); font-size: 15px; line-height: 1.35; }
  .contact__name { color: var(--name-red); font-weight: 500; font-size: 22px; line-height: 1.1; }
  .contact__role { font-size: 14px; margin-bottom: 14px; }
  .contact__address { margin-bottom: 14px; }
  .contact__row { display: flex; align-items: center; gap: 8px; }
  .contact__row svg { width: 12px; height: 12px; fill: var(--brand-red); flex: none; }
</style>
</head>
<body>
  <section class="card card--front" aria-label="Card front">
    <div class="brand">
      <span class="brand__dot"></span>
      <span class="brand__name">plintovo</span>
    </div>
  </section>

  <section class="card card--back" aria-label="Card back">
    <div class="brand">
      <span class="brand__dot"></span>
      <span class="brand__name">plintovo</span>
    </div>
    <div class="divider"></div>
    <div class="contact">
      <p class="contact__name">Marlen Oakes</p>
      <p class="contact__role">Manager</p>
      <p class="contact__address">Your address, city<br>state, ZIP 0000</p>
      <p class="contact__row">
        <svg viewBox="0 0 12 12" aria-hidden="true"><path d="M2.5 0.8l2 2.2-1 1.3c.7 1.6 2 2.9 3.6 3.6l1.3-1 2.2 2-1.2 2C5.3 11 1 6.7 0.9 2z"/></svg>
        555-014-2100
      </p>
      <p class="contact__row">
        <svg viewBox="0 0 12 12" aria-hidden="true"><path d="M0.5 2.5h11v7h-11z M1 3l5 3.6L11 3" stroke="#fff" stroke-width="0.8"/></svg>
        hello@plintovo.com
      </p>
      <p class="contact__row">
        <svg viewBox="0 0 12 12" aria-hidden="true"><circle cx="6" cy="6" r="5.5"/><path d="M0.5 6h11M6 0.5c-2.5 3-2.5 8 0 11M6 0.5c2.5 3 2.5 8 0 11" stroke="#fff" stroke-width="0.8" fill="none"/></svg>
        www.plintovo.com
      </p>
    </div>
  </section>
</body>
</html>
```